The Copper Compass

we require a classy business card design for a business coaching company that uses our current logo and the wording:

Front of card:

LOGO
Glen Halvorsen
CEO
TEL: 1300 4 21953
FAX: 1300 6 21953
Mobile: 0419 627184
PO Box 217, Larkfield Rise, Brisbane, Qld 4163
e: glenh@coppercx.com.au
w: www.coppercx.com.au

Reverse side of the card:

Systematizing Businesses into Turnkey Operations
Strategic Business Plans
Sales & Marketing Programs
Sales Training & Business Coaching
Internet Marketing & Web Design

Here’s what our clients say:

“We grew from $396,000 to over $5million in 4 years and made QMT’s Rising Enterprise Honour Roll 3 years running!” – Simon Kearney, Meridel Works

small to medium sized business owners in Australia

Business

• standard business card size

```html
<!DOCTYPE html>
<html lang="en">
<head>
<meta charset="utf-8">
<title>The Copper Compass – Business Card</title>
<link rel="stylesheet" href="https://fonts.googleapis.com/css2?family=Audiowide&family=Questrial&family=Tinos&display=swap">
<style>
  :root {
    --page: #ffffff;
    --ink: #111111;
    --amber: #f8b800;
    --amber-soft: #fde3a6;
    --name-orange: #f39a12;
    --steel-dark: #5e5e60;
    --steel-mid: #b5b6b9;
    --steel-light: #f8f8f8;
    --card-edge: #7a7a7a;
  }
  * { box-sizing: border-box; margin: 0; padding: 0; }
  html, body {
    width: 848px; height: 1200px; overflow: hidden;
    background: var(--page);
  }
  .sheet { position: relative; width: 848px; height: 1200px; }

  .card {
    position: absolute;
    left: 238px; width: 356px; height: 217px;
    border: 0.6px solid var(--card-edge);
    font-family: "Questrial", sans-serif;
    color: var(--ink);
    overflow: hidden;
  }
  .card--front { top: 395px; background: var(--page); }
  .card--back {
    top: 619px;
    background: radial-gradient(ellipse 62% 78% at 51% 52%, #ffffff 0%, var(--amber-soft) 40%, var(--amber) 100%);
  }

  .header-band {
    position: absolute; left: 0; top: 0; width: 100%; height: 49px;
    background: linear-gradient(90deg, var(--steel-dark) 0%, var(--steel-mid) 22%, var(--steel-light) 50%, var(--steel-mid) 78%, var(--steel-dark) 100%);
  }
  .accent-stripe {
    position: absolute; left: 0; top: 49px; width: 100%; height: 7px;
    background: linear-gradient(90deg, var(--amber) 0%, var(--amber) 28%, #feedc4 50%, var(--amber) 72%, var(--amber) 100%);
  }
  .brand-name {
    position: absolute; left: 13px; top: 18px;
    font-family: "Questrial", sans-serif;
    font-size: 12px; color: var(--ink);
    letter-spacing: 0.1px;
  }

  .person-name {
    position: absolute; left: 10px; top: 89px;
    font-family: "Audiowide", sans-serif;
    font-style: italic;
    font-size: 15px; letter-spacing: 0.6px;
    color: var(--name-orange);
  }
  .person-title {
    position: absolute; left: 10px; top: 107px;
    font-family: "Tinos", serif; font-size: 10.5px;
  }

  .contact-block {
    position: absolute; right: 9px; top: 92px;
    text-align: right; font-size: 10px; line-height: 14px;
    list-style: none;
  }
  .web-line {
    position: absolute; top: 189px; font-size: 9.5px;
  }
  .web-line--email { left: 10px; }
  .web-line--site { right: 9px; }

  .service-list {
    position: absolute; left: 10px; top: 22px;
    list-style: none; font-size: 10px; line-height: 14px;
  }
  .service-list li { position: relative; padding-left: 25px; }
  .service-list li::before {
    content: "•"; position: absolute; left: 0; top: 0; font-size: 9px;
  }
  .testimonial-intro {
    position: absolute; left: 9px; top: 149px; font-size: 8.5px;
  }
  .testimonial-quote {
    position: absolute; left: 9px; top: 176px; width: 330px;
    font-size: 8.5px; line-height: 14px;
  }
</style>
</head>
<body>
<main class="sheet">
  <section class="card card--front" aria-label="Front of card">
    <div class="header-band"></div>
    <div class="accent-stripe"></div>
    <div class="brand-name">The Copper Compass</div>

    <h1 class="person-name">Glen Halvorsen</h1>
    <p class="person-title">CEO</p>

    <ul class="contact-block">
      <li>PO Box 217,</li>
      <li>Larkfield Rise,</li>
      <li>Brisbane, Qld 4163</li>
      <li>TEL: 1300 4 21953</li>
      <li>FAX: 1300 6 21953</li>
      <li>Mobile: 0419 627184</li>
    </ul>

    <p class="web-line web-line--email">E-mail: glenh@coppercx.com.au</p>
    <p class="web-line web-line--site">Website: www.coppercx.com.au</p>
  </section>

  <section class="card card--back" aria-label="Back of card">
    <ul class="service-list">
      <li>Systematizing Businesses into Turnkey Operations</li>
      <li>Strategic Business Plans</li>
      <li>Sales &amp; Marketing Programs</li>
      <li>Sales Training &amp; Business Coaching</li>
      <li>Internet Marketing &amp; Web Design</li>
    </ul>
    <p class="testimonial-intro">Here’s what our clients say:</p>
    <p class="testimonial-quote">“We grew from $396,000 to over $5million in 4 years and made QMT’s Rising Enterprise Honour Roll 3 years running!” – Simon Kearney, Meridel Works</p>
  </section>
</main>
</body>
</html>
```